New Infographic Design Project

I need a 1 page Infographic that explains our Velqor Strand offer.

Can you use the following content in the attached document to create a 1 page infographic. The image in the bottom of the document is one of our competitors who is offering the same thing, this image is only provided for inspiration and ideas as we need ours to be based on the content of the document and aligned with the Bruvell Brand

```html
<!DOCTYPE html>
<html lang="en">
<head>
<meta charset="utf-8">
<title>Data Ready. AI Ready. In 6 Weeks.</title>
<link rel="stylesheet" href="https://fonts.googleapis.com/css2?family=Archivo:wdth,wght@125,900&family=Barlow+Condensed:ital,wght@0,600;1,700;1,800&family=Figtree:ital,wght@0,400;1,700;1,800&display=swap">
<style>
:root{
  --ink:#0b0b0b;
  --white:#ffffff;
  --blue:#29abe2;
  --blue-deep:#1e8ccd;
  --grey-band:#e9e9e9;
  --w1:#d7e9f7;
  --w2:#bcdcf3;
  --w3:#9ccdef;
  --w4:#74bde9;
  --w5:#2aa8e1;
  --w6:#1f8ecf;
}
*{box-sizing:border-box;margin:0;padding:0}
html,body{width:1200px;height:848px;overflow:hidden;background:var(--white)}
body{font-family:"Figtree",sans-serif;color:var(--ink)}
.canvas{position:relative;width:1200px;height:848px;overflow:hidden}

/* intro */
.hero-title{position:absolute;left:58px;top:36px;font-family:"Barlow Condensed",sans-serif;font-style:italic;font-weight:800;font-size:82px;line-height:66px;letter-spacing:-1px;text-transform:uppercase}
.hero-underline{position:absolute;left:116px;top:248px;width:228px;height:6px;border-radius:3px;background:var(--blue)}
.quote-mark{position:absolute;left:412px;top:52px;width:104px;height:80px}
.partner-title{position:absolute;left:551px;top:60px;font-family:"Archivo",sans-serif;font-stretch:125%;font-weight:900;font-size:31px;line-height:38px;letter-spacing:.5px;text-transform:uppercase}
.partner-copy{position:absolute;left:413px;top:150px;width:730px;font-size:14.6px;line-height:22.8px}

/* edge band */
.edge-band{position:absolute;left:0;top:272px;width:1200px;height:168px;background:linear-gradient(180deg,var(--grey-band),#fafafa)}
.edge-heading{position:absolute;left:0;top:12px;width:1200px;text-align:center;font-family:"Archivo",sans-serif;font-stretch:125%;font-weight:900;font-size:34px;letter-spacing:1px}
.edge-arrow{position:absolute;top:20px;width:290px;height:12px}
.edge-arrow.left{left:50px}
.edge-arrow.right{left:880px}
.edge-item{position:absolute;top:60px}
.edge-item svg{position:absolute;left:0;top:0;width:38px;height:42px}
.edge-item h3{position:absolute;top:2px;font-style:italic;font-weight:700;font-size:15.5px;line-height:17px;white-space:nowrap}
.edge-item p{position:absolute;top:46px;font-size:13px;line-height:17px}

/* timeline */
.value-band{position:absolute;left:0;top:440px;width:1200px;height:268px}
.week-col{position:absolute;top:0;height:268px}
.value-strip{position:absolute;left:0;top:0;width:1200px;height:62px;background:linear-gradient(90deg,#e9f3fb 0%,#c3e0f4 35%,#7fbfe8 70%,#3d94d3 100%)}
.value-heading{position:absolute;left:50px;top:-6px;width:1100px;font-family:"Archivo",sans-serif;font-stretch:125%;font-weight:900;font-size:64px;letter-spacing:2px;white-space:nowrap;word-spacing:8px}
.timeline-line{position:absolute;left:54px;top:114px;width:1083px;height:3px;background:var(--ink)}
.timeline-dot{position:absolute;top:110px;width:11px;height:11px;border-radius:50%;background:var(--ink)}
.week{position:absolute;top:78px;width:180px}
.week-label{font-family:"Barlow Condensed",sans-serif;font-weight:600;font-size:24px;line-height:28px;letter-spacing:-.3px}
.week-title{margin-top:20px;font-style:italic;font-weight:700;font-size:14.6px;line-height:15.5px}
.week-copy{margin-top:7px;font-size:12.2px;line-height:14.3px}

/* extra edge */
.extra-band{position:absolute;left:0;top:708px;width:1200px;height:140px;background:var(--ink);color:var(--white)}
.extra-title{position:absolute;left:48px;top:14px;font-family:"Barlow Condensed",sans-serif;font-style:italic;font-weight:800;font-size:54px;line-height:50px;text-transform:uppercase}
.extra-title span{display:block;padding-left:28px}
.extra-item{position:absolute;top:30px}
.extra-item h4{font-weight:400;font-size:14.6px;color:var(--blue);letter-spacing:-.1px}
.extra-item p{margin-top:6px;font-size:12.1px;line-height:15.6px}
</style>
</head>
<body>
<main class="canvas">

  <h1 class="hero-title">Data Ready.<br>AI Ready.<br>In 6 Weeks.</h1>
  <div class="hero-underline"></div>

  <svg class="quote-mark" viewBox="0 0 104 80" aria-hidden="true">
    <path d="M8 0h28l-10 40h10v40H0V40L8 0z" fill="var(--blue)"/>
    <path d="M68 0h28l-10 40h10v40H60V40L68 0z" fill="var(--blue)"/>
  </svg>

  <h2 class="partner-title">Your Long-Term<br>Strategic Data Partner</h2>
  <p class="partner-copy">We start with a Business Data Assessment or Velqor Strand Deployment Assessment to pinpoint the highest-value use cases, the biggest data risks, and the fastest path to impact. We stand up a governed Velqor Strand foundation using repeatable ingestion, validation, and common data model patterns, so your reporting scales cleanly and your AI initiatives provide business value.</p>

  <section class="edge-band">
    <svg class="edge-arrow left" viewBox="0 0 290 12" aria-hidden="true"><line x1="4" y1="6" x2="290" y2="6" stroke="var(--ink)" stroke-width="1.6"/><path d="M0 6l16-5v10z" fill="var(--ink)"/></svg>
    <h2 class="edge-heading">THE BRUVELL EDGE</h2>
    <svg class="edge-arrow right" viewBox="0 0 290 12" aria-hidden="true"><line x1="0" y1="6" x2="286" y2="6" stroke="var(--ink)" stroke-width="1.6"/><path d="M290 6l-16-5v10z" fill="var(--ink)"/></svg>

    <div class="edge-item" style="left:62px">
      <svg viewBox="0 0 38 42" aria-hidden="true"><path d="M10 24l-6 14 7-2 3 6 5-12zM28 24l6 14-7-2-3 6-5-12z" fill="var(--blue)"/><circle cx="19" cy="16" r="15" fill="var(--blue)"/><circle cx="19" cy="16" r="10" fill="#fff"/><circle cx="19" cy="16" r="7.5" fill="var(--blue)"/></svg>
      <h3 style="left:46px">Quality-first<br>Delivery</h3>
      <p style="width:270px">Automated validation, data tests, and “quality gates” that stop bad data upstream.</p>
    </div>
    <div class="edge-item" style="left:348px">
      <svg viewBox="0 0 38 42" aria-hidden="true"><path d="M19 4l18 8-18 8-18-8z" fill="var(--blue)"/><path d="M4 18l15 7 15-7 3 2-18 8-18-8z" fill="var(--blue)"/><path d="M4 26l15 7 15-7 3 2-18 8-18-8z" fill="var(--blue)"/></svg>
      <h3 style="left:53px">Data Products,<br>Not Datasets</h3>
      <p style="width:290px;left:2px">Clear ownership, SLAs, versioning, and reusable, consumable outputs aligned to high impact business outcomes.</p>
    </div>
    <div class="edge-item" style="left:662px">
      <svg viewBox="0 0 38 42" aria-hidden="true"><rect x="1" y="18" width="8" height="20" rx="1.5" fill="var(--blue)"/><path d="M12 18l8-14c3-2 6 0 5 4l-2 9h10c3 0 4 3 3 5l-4 14c-1 2-2 3-4 3H12z" fill="var(--blue)"/></svg>
      <h3 style="left:46px">Governance That<br>Doesn’t Slow You Down</h3>
      <p style="width:270px;left:1px">Security, access, lineage, and auditability built in from day one.</p>
    </div>
    <div class="edge-item" style="left:936px">
      <svg viewBox="0 0 38 42" aria-hidden="true"><g transform="translate(19 20)" fill="var(--blue)"><rect x="-4" y="-18" width="8" height="36" rx="1.5"/><rect x="-4" y="-18" width="8" height="36" rx="1.5" transform="rotate(45)"/><rect x="-4" y="-18" width="8" height="36" rx="1.5" transform="rotate(90)"/><rect x="-4" y="-18" width="8" height="36" rx="1.5" transform="rotate(135)"/><circle r="12"/><circle r="5.5" fill="#fff"/></g></svg>
      <h3 style="left:43px">Operate<br>Seamlessly</h3>
      <p style="width:220px;left:2px">CI/CD, monitoring, and cost controls so the platform stays healthy.</p>
    </div>
  </section>

  <section class="value-band">
    <div class="week-col" style="left:0;width:218px;background:var(--w1)"></div>
    <div class="week-col" style="left:218px;width:186px;background:var(--w2)"></div>
    <div class="week-col" style="left:404px;width:182px;background:var(--w3)"></div>
    <div class="week-col" style="left:586px;width:184px;background:var(--w4)"></div>
    <div class="week-col" style="left:770px;width:182px;background:var(--w5)"></div>
    <div class="week-col" style="left:952px;width:248px;background:var(--w6)"></div>
    <div class="value-strip"></div>
    <h2 class="value-heading">6 WEEK TIME TO VALUE</h2>

    <div class="timeline-line"></div>
    <div class="timeline-dot" style="left:49px"></div>
    <div class="timeline-dot" style="left:213px"></div>
    <div class="timeline-dot" style="left:399px"></div>
    <div class="timeline-dot" style="left:581px"></div>
    <div class="timeline-dot" style="left:765px"></div>
    <div class="timeline-dot" style="left:947px"></div>
    <div class="timeline-dot" style="left:1132px"></div>

    <div class="week" style="left:53px;width:165px">
      <div class="week-label">WEEK 1</div>
      <div class="week-title">Envision<br>&amp; Assess</div>
      <p class="week-copy">Use case shortlist and priority based on highest business impact, current-state review, data risk &amp; compliance priorities, target operating model.</p>
    </div>
    <div class="week" style="left:234px">
      <div class="week-label">WEEK 2</div>
      <div class="week-title">Architecture &amp;<br>governance design</div>
      <p class="week-copy">Landing zone decisions, security and access model, patterns/ standards, delivery plan and success metrics.</p>
    </div>
    <div class="week" style="left:416px">
      <div class="week-label">WEEK 3</div>
      <div class="week-title">Strand foundation<br>deployed</div>
      <p class="week-copy">Workspaces and environments, automation &amp; CI/CD, onboarding playbooks, baseline policies/guardrails.</p>
    </div>
    <div class="week" style="left:598px">
      <div class="week-label">WEEK 4</div>
      <div class="week-title">Data ingestion +<br>validation framework</div>
      <p class="week-copy">Reusable ingestion patterns, automated validation, data contracts/SLAs, observability signals and alerting.</p>
    </div>
    <div class="week" style="left:780px">
      <div class="week-label">WEEK 5</div>
      <div class="week-title">Scalable common<br>data model</div>
      <p class="week-copy">Domain model, master entities, curated layer, semantic modelling patterns that support Lumetric BI at scale.</p>
    </div>
    <div class="week" style="left:962px;width:200px">
      <div class="week-label">WEEK 6</div>
      <div class="week-title">Business outcomes +<br>AI-ready capability</div>
      <p class="week-copy">Executive dashboards and priority reports, performance optimisation, hypercare and handover, AI readiness check and pilot plan (predictive analytics and/or secure enterprise LLM).</p>
    </div>
  </section>

  <section class="extra-band">
    <h2 class="extra-title">Extra<span>Edge</span></h2>
    <div class="extra-item" style="left:209px;width:220px">
      <h4>“AI-ready data” guarantee</h4>
      <p>Every priority dataset ships with validation rules, ownership, lineage, and freshness SLAs before it can power AI.</p>
    </div>
    <div class="extra-item" style="left:461px;width:200px">
      <h4>Cost-to-serve transparency</h4>
      <p>Show business owners what each product/report costs to run and optimise it continuously.</p>
    </div>
    <div class="extra-item" style="left:692px;width:220px">
      <h4>Change-proof pipelines</h4>
      <p>Data contracts + automated tests reduce breakages from upstream schema changes.</p>
    </div>
    <div class="extra-item" style="left:942px;width:220px">
      <h4>Governed self-serve</h4>
      <p>Catalog + certified datasets so teams move faster without creating data chaos.</p>
    </div>
  </section>

</main>
</body>
</html>
```